Harborline Security and Surveillance Business Card

Business Card Design - Company Name:Freedom Security and SurveillanceWe are a Security Systems Integrator Specializing in Security Systems/ Video Surveillance and Access Control. Our areas of expertise are:Security SystemsVideo SurveillanceAccess ControlFire Alarm SystemsNetwork CablingCellular BoostersMy input is the Front of the Card is: logo, name of Business, My Name, Phone Number, and email.Rear of Card is the 6 areas of expertise, I just dont want the front to be very busy.
Name: Tom Werner
Title: President
Email: tom@harborlinesecsys.example
website: harborlinesecsys.example

```html
<!DOCTYPE html>
<html lang="en">
<head>
<meta charset="utf-8">
<title>Harborline Security and Surveillance – Business Card</title>
<link rel="stylesheet" href="https://fonts.googleapis.com/css2?family=Michroma&family=Montserrat:wght@500;700&family=Roboto:wght@400;500&display=swap">
<style>
  :root {
    --backdrop: #2b2b2b;
    --card-white: #f7f7f7;
    --brand-blue: #1a5bb5;
    --swoosh-grey: #a9acb0;
    --text-grey: #4a4a4a;
    --ink-white: #ffffff;
  }
  * { box-sizing: border-box; margin: 0; padding: 0; }
  html, body {
    width: 1200px; height: 997px; overflow: hidden;
    background: var(--backdrop);
  }
  .stage { position: relative; width: 1200px; height: 997px; }
  .card {
    position: absolute;
    width: 500px; height: 286px;
    border-radius: 18px;
    overflow: hidden;
    background: var(--card-white);
    box-shadow: 0 14px 30px rgba(0,0,0,.45);
  }
  .card-back { left: 60px; top: 356px; }
  .card-front { left: 640px; top: 356px; }
  .card-art { position: absolute; inset: 0; width: 100%; height: 100%; }

  .wordmark {
    position: absolute;
    font-family: "Michroma", sans-serif;
    font-weight: 400;
    color: var(--brand-blue);
    text-align: center;
    line-height: 1.1;
  }
  .wordmark-main { display: block; font-size: 22px; letter-spacing: 1px; }
  .wordmark-sub { display: block; font-size: 10px; letter-spacing: 6px; margin-top: 3px; }
  .brand-dot {
    display: inline-block; width: 14px; height: 14px; border-radius: 50%;
    background: var(--brand-blue); margin-bottom: 8px;
  }

  /* front */
  .card-front .wordmark { left: 0; right: 0; top: 36px; }
  .holder { position: absolute; left: 0; right: 0; top: 146px; text-align: center; }
  .holder-name {
    font-family: "Montserrat", sans-serif; font-weight: 700;
    font-size: 17px; color: var(--brand-blue); letter-spacing: .5px;
  }
  .holder-title {
    font-family: "Roboto", sans-serif; font-size: 12px; color: var(--text-grey);
  }
  .contact {
    position: absolute;
    font-family: "Roboto", sans-serif;
    display: flex; flex-direction: column; gap: 6px;
  }
  .contact svg { width: 20px; height: 20px; }
  .contact-mail {
    right: 22px; top: 92px; align-items: flex-end;
    font-size: 13px; color: var(--brand-blue);
  }
  .contact-phone {
    left: 22px; bottom: 20px; align-items: flex-start;
    font-size: 15px; color: var(--ink-white);
  }

  /* back */
  .card-back .wordmark { right: 24px; top: 34px; text-align: right; }
  .card-back .wordmark-main { font-size: 20px; }
  .expertise {
    position: absolute; left: 34px; right: 24px; top: 170px;
    font-family: "Roboto", sans-serif; color: var(--ink-white);
  }
  .expertise-lead {
    font-weight: 500; font-size: 12px; text-decoration: underline;
    text-align: center; margin-bottom: 10px;
  }
  .expertise-list {
    list-style: none;
    display: grid; grid-template-columns: repeat(3, auto);
    column-gap: 22px; row-gap: 6px; font-size: 14px;
  }
</style>
</head>
<body>
<main class="stage">

  <section class="card card-back" aria-label="Card back">
    <svg class="card-art" viewBox="0 0 500 286" aria-hidden="true">
      <path d="M0,190 Q250,130 500,95 L500,286 L0,286 Z" fill="var(--brand-blue)"/>
      <path d="M0,178 Q250,118 500,83" fill="none" stroke="var(--swoosh-grey)" stroke-width="6"/>
    </svg>
    <div class="wordmark">
      <span class="wordmark-main"><span class="brand-dot"></span> HARBORLINE SECURITY</span>
      <span class="wordmark-sub">AND SURVEILLANCE</span>
    </div>
    <div class="expertise">
      <p class="expertise-lead">Our areas of expertise are:</p>
      <ul class="expertise-list">
        <li>Security Systems</li>
        <li>Video Surveillance</li>
        <li>Access Control</li>
        <li>Fire Alarm Systems</li>
        <li>Network Cabling</li>
        <li>Cellular Boosters</li>
      </ul>
    </div>
  </section>

  <section class="card card-front" aria-label="Card front">
    <svg class="card-art" viewBox="0 0 500 286" aria-hidden="true">
      <path d="M0,190 Q250,270 500,165 L500,286 L0,286 Z" fill="var(--brand-blue)"/>
      <path d="M0,176 Q250,256 500,151" fill="none" stroke="var(--swoosh-grey)" stroke-width="6"/>
    </svg>
    <div class="wordmark">
      <span class="wordmark-main"><span class="brand-dot"></span> HARBORLINE SECURITY</span>
      <span class="wordmark-sub">AND SURVEILLANCE</span>
    </div>
    <div class="contact contact-mail">
      <svg viewBox="0 0 20 20" aria-hidden="true">
        <circle cx="10" cy="10" r="10" fill="var(--brand-blue)"/>
        <rect x="5" y="6.5" width="10" height="7" fill="var(--ink-white)"/>
        <path d="M5,6.5 L10,10.5 L15,6.5" fill="none" stroke="var(--brand-blue)" stroke-width="1"/>
      </svg>
      <span>tom@harborlinesecsys.example</span>
    </div>
    <div class="holder">
      <p class="holder-name">TOM WERNER</p>
      <p class="holder-title">President</p>
    </div>
    <div class="contact contact-phone">
      <svg viewBox="0 0 20 20" aria-hidden="true">
        <circle cx="10" cy="10" r="10" fill="var(--ink-white)"/>
        <path d="M6,7 Q10,4.5 14,7 L13,8.5 L11.5,8 L11.5,7 L8.5,7 L8.5,8 L7,8.5 Z" fill="var(--brand-blue)"/>
        <rect x="6.5" y="9.5" width="7" height="5" rx="1" fill="var(--brand-blue)"/>
      </svg>
      <span>555-016-2300</span>
    </div>
  </section>

</main>
</body>
</html>
```